Lumen QRX - Website

Lumen QRX is a online marketing solutions Agency, working with top partners within the industry to deliver online customers to Digital campaigns.

Our current site is www.lumenqrx-example.com (Apart from the logo, there is NOTHING we like about this site - please do not repeat anything from this site)

Specification of website:

- Modern, and light refreshing look. Corporate and neutral designs.

-Keep our logo - colour theme: Green/grey - hint of Orange/Blue

- The only text we would like on the Homepage is: Performance based online marketing specialists, driving incremental sales globally

and...

These are headings we would like people to do: Affiliate Marketing, Email marketing, Lead Generation, Social media marketing, Search Engine Marketing, Incentive Marketing (there is no need for the detailed text of these topics to be on front page, these can be linked into another page for those who seeks further info)

Images: Have images to show what we do.. keep it neat and professional/simple and stylish.

Please contact us if you have any questions at all.

Thank you for taking time our with our project!

Good luck all!

Regards

Lumen QRX
Updates

Hello Designers,

Thank you to all who have taken time out working on our project. We have been very happy with the quality and level of prompt feedback.

Unfortunately we could only choose one, and VelBoro's designed is most suited for our company branding. So, Congratulations VelBoro.

Once again, thank you all.

Kindest regards,

Lumen QRX

Target Market(s)

Clients: Fizzo, Torvik, Lunto, panelo.example, Brevard Hotel...

Industry/Entity Type

Marketing

Requirements
Must have
• User friendly
Nice to have
• We operate Internationally, so a generic feel for EU/UK/US would be ideal...
Should not have
• Should not look like www.lumenqrx-example.com

```html
<!DOCTYPE html>
<html lang="en">
<head>
<meta charset="utf-8">
<title>Lumen QRX – Performance based online marketing</title>
<link rel="stylesheet" href="https://fonts.googleapis.com/css2?family=Lustria&family=Arimo:wght@400&display=swap">
<style>
  :root {
    --green: #6f9a12;
    --green-light: #93bd34;
    --green-text: #8cb43a;
    --orange: #f7901e;
    --orange-dark: #f07a10;
    --blue: #3c9bd4;
    --blue-dark: #2a86c2;
    --red: #b3060c;
    --red-dark: #a30008;
    --grey-mid: #b8b8b8;
    --grey-line: #c9c9c9;
    --brand-text: #5a5a5a;
    --footer-bg: #e4e4e4;
    --footer-text: #444;
    --white: #fff;
  }
  * { box-sizing: border-box; margin: 0; padding: 0; }
  html, body { width: 1200px; height: 852px; overflow: hidden; }
  body {
    position: relative;
    font-family: "Lustria", serif;
    background: linear-gradient(to bottom, var(--grey-mid) 326px, #d9d9d9 520px, #f7f7f7 740px, var(--white) 760px);
  }
  .site-header {
    position: absolute; left: 0; top: 0; width: 1200px; height: 125px;
    background: linear-gradient(to bottom, #a9a9a9 0, #dcdcdc 10px, #d4d4d4 100%);
  }
  .header-grid {
    position: absolute; inset: 0;
    background-image:
      repeating-linear-gradient(to right, rgba(255,255,255,.35) 0 1px, transparent 1px 14px),
      repeating-linear-gradient(to bottom, rgba(255,255,255,.35) 0 1px, transparent 1px 14px);
  }
  .brand {
    position: absolute; left: 93px; top: 38px;
    font-size: 44px; color: var(--brand-text); line-height: 1;
  }
  .quote-button {
    position: absolute; left: 902px; top: 0; width: 176px; height: 36px;
    background: var(--orange);
    border: 1px dashed rgba(255,255,255,.7); border-top: 0;
    display: flex; align-items: center; justify-content: center; gap: 10px;
    color: var(--white); font-size: 17px; text-decoration: none;
  }
  .main-band {
    position: absolute; left: 0; top: 125px; width: 1200px; height: 201px;
    background: linear-gradient(to bottom, var(--green-light) 0, var(--green) 45px, var(--green) 100%);
  }
  .main-nav {
    position: absolute; left: 71px; top: 125px; height: 73px;
    display: flex;
  }
  .main-nav a {
    display: flex; align-items: center; justify-content: center;
    height: 73px; color: #eef5df; font-size: 16px; text-decoration: none;
    border-left: 1px dotted rgba(255,255,255,.6);
  }
  .main-nav a:last-child { border-right: 1px dotted rgba(255,255,255,.6); }
  .hero {
    position: absolute; left: 58px; top: 198px; width: 1059px; height: 264px;
    background: var(--white); border-radius: 10px;
  }
  .hero-text {
    position: absolute; left: 84px; top: 64px;
    color: var(--green-text); font-size: 31px; line-height: 44px;
  }
  .hero-text .accent { color: var(--orange); }
  .hero-text .line-1 { padding-left: 4px; }
  .hero-art {
    position: absolute; left: 704px; top: 17px; width: 244px; height: 240px;
    border-radius: 50%;
    background: radial-gradient(circle at 45% 45%, #cfe6a6 0, #b9d7ee 40%, #f6c48c 70%, var(--white) 72%);
  }
  .hero-arrow { position: absolute; top: 308px; }
  .hero-arrow.prev { left: 82px; }
  .hero-arrow.next { left: 1062px; }
  .services {
    position: absolute; left: 59px; top: 501px;
    display: flex; gap: 15px;
  }
  .service-card {
    position: relative; width: 254px; height: 235px; background: var(--white);
  }
  .service-card::before {
    content: ""; position: absolute; left: 18px; top: -1px;
    border-left: 9px solid transparent; border-right: 9px solid transparent;
    border-top: 10px solid #dcdcdc;
  }
  .service-title {
    margin: 14px 14px 0; padding-bottom: 3px;
    font-size: 20px; font-weight: 400; white-space: nowrap;
    border-bottom: 1px solid #e2e2e2;
  }
  .service-art {
    position: absolute; left: 10px; top: 48px; width: 234px; height: 152px;
  }
  .service-more {
    position: absolute; left: 0; bottom: 0; width: 254px; height: 32px;
    display: flex; align-items: center; gap: 8px; padding-left: 10px;
    color: var(--white); font-size: 14px; text-decoration: none;
  }
  .affiliate .service-title { color: var(--green-text); }
  .affiliate .service-art { background: radial-gradient(ellipse at center, #4f8a1c 0, #7fb43f 45%, #f4f8ee 75%); }
  .affiliate .service-more { background: linear-gradient(var(--green-light), var(--green)); }
  .lead .service-title { color: var(--orange); }
  .lead .service-art { background: radial-gradient(ellipse at center, #f26a1b 0, #f59a5c 40%, #f1f1f1 72%); }
  .lead .service-more { background: linear-gradient(var(--orange), var(--orange-dark)); }
  .search .service-title { color: var(--blue); }
  .search .service-art { background: radial-gradient(circle at center, #2f8fd0 0, #9fd0ef 42%, #ffffff 66%); }
  .search .service-more { background: linear-gradient(var(--blue), var(--blue-dark)); }
  .social .service-title { color: var(--red); }
  .social .service-art { background: radial-gradient(circle at center, #c8161c 0, #e77a7d 36%, #ffffff 62%); }
  .social .service-more { background: linear-gradient(var(--red), var(--red-dark)); }
  .site-footer {
    position: absolute; left: 0; top: 760px; width: 1200px; height: 92px;
    background: var(--footer-bg); border-top: 1px solid var(--grey-line);
    font-family: "Arimo", sans-serif; color: var(--footer-text);
  }
  .footer-nav {
    position: absolute; top: 29px; left: 0; width: 1200px;
    display: flex; justify-content: center; font-size: 11px;
  }
  .footer-nav a { color: var(--footer-text); text-decoration: none; }
  .footer-nav .sep { margin: 0 27px; }
  .copyright {
    position: absolute; top: 57px; left: 0; width: 1200px;
    text-align: center; font-size: 10.5px;
  }
</style>
</head>
<body>
  <header class="site-header">
    <div class="header-grid"></div>
    <div class="brand">Lumen QRX</div>
    <a class="quote-button" href="#">
      <svg width="14" height="22" viewBox="0 0 14 22" aria-hidden="true"><path d="M3 1 L7 1 L8 6 L5 8 Q6 13 9 15 L12 13 L14 17 L11 21 Q2 18 1 5 Z" fill="#fff"/></svg>
      Get a Quote !
    </a>
  </header>

  <div class="main-band"></div>
  <nav class="main-nav">
    <a href="#" style="width:108px">home</a>
    <a href="#" style="width:129px">about us</a>
    <a href="#" style="width:148px">what we do</a>
    <a href="#" style="width:128px">our work</a>
    <a href="#" style="width:164px">work with us</a>
    <a href="#" style="width:134px">contact us</a>
  </nav>

  <section class="hero">
    <p class="hero-text">
      <span class="line-1">Performance based</span><br>
      <span class="accent">ONLINE MARKETING</span> specialists,<br>
      driving incremental sales globally
    </p>
    <div class="hero-art" role="img" aria-label="Illustration of three colourful figures standing on joined puzzle pieces"></div>
  </section>
  <svg class="hero-arrow prev" width="30" height="48" viewBox="0 0 30 48" aria-hidden="true"><polyline points="26,3 5,24 26,45" fill="none" stroke="#d8dde0" stroke-width="5"/></svg>
  <svg class="hero-arrow next" width="30" height="48" viewBox="0 0 30 48" aria-hidden="true"><polyline points="4,3 25,24 4,45" fill="none" stroke="#d8dde0" stroke-width="5"/></svg>

  <main class="services">
    <article class="service-card affiliate">
      <h2 class="service-title">Affiliate Marketing</h2>
      <div class="service-art" role="img" aria-label="Green word cloud of internet marketing terms"></div>
      <a class="service-more" href="#">more info <svg width="6" height="8" viewBox="0 0 6 8"><path d="M0 0 L6 4 L0 8Z" fill="#fff"/></svg></a>
    </article>
    <article class="service-card lead">
      <h2 class="service-title">Lead Generation</h2>
      <div class="service-art" role="img" aria-label="Orange 3D letters with gears"></div>
      <a class="service-more" href="#">more info <svg width="6" height="8" viewBox="0 0 6 8"><path d="M0 0 L6 4 L0 8Z" fill="#fff"/></svg></a>
    </article>
    <article class="service-card search">
      <h2 class="service-title">Search Eng Marketing</h2>
      <div class="service-art" role="img" aria-label="Blue globe with a marketing arrow around it"></div>
      <a class="service-more" href="#">more info <svg width="6" height="8" viewBox="0 0 6 8"><path d="M0 0 L6 4 L0 8Z" fill="#fff"/></svg></a>
    </article>
    <article class="service-card social">
      <h2 class="service-title">Social Media Marketing</h2>
      <div class="service-art" role="img" aria-label="Red target with a dart in the bullseye"></div>
      <a class="service-more" href="#">more info <svg width="6" height="8" viewBox="0 0 6 8"><path d="M0 0 L6 4 L0 8Z" fill="#fff"/></svg></a>
    </article>
  </main>

  <footer class="site-footer">
    <nav class="footer-nav">
      <a href="#">Home</a><span class="sep">|</span>
      <a href="#">About Us</a><span class="sep">|</span>
      <a href="#">What we Do</a><span class="sep">|</span>
      <a href="#">Our work</a><span class="sep">|</span>
      <a href="#">Work with us</a><span class="sep">|</span>
      <a href="#">Contact Us</a>
    </nav>
    <p class="copyright">Copyright © 2010 Lumen QRX. All Rights Reserved.</p>
  </footer>
</body>
</html>
```